Design a Flyer

Sunlit Melody Retreat
Hosted by The Tuneful Attic

Sunlit Melody retreat will run June through July. 4 days a week with two sessions a day.

Monday- Thursday
Cost is $99.00 per session per week. with 25 registration fee

Morning Session 9am-12pm
Afternoon Session 1pm-4pm

June Sessions July Sessions
4th-7th 9th-12th
11th-16th 16th-19th
18th-21st 23th-26th
25th-28th

Students will have the option to choose between the following classes.

● Vocal
● Guitar
● Bass
● Drums
● Violin
● Rock Band
● Sound Mixing
● Video Making
● DJ /Mixing
● Song Writing
● Recording
● Hip-Hop Boot Camp

Space is limited, campers are allowed to sign up for morning and afternoon sessions, campers will need to bring their own lunch if taking both sessions.

will need at least 4 sizes at handover or completed

```html
<!DOCTYPE html>
<html lang="en">
<head>
<meta charset="utf-8">
<title>Sunlit Melody Retreat – Flyer</title>
<link rel="stylesheet" href="https://fonts.googleapis.com/css2?family=Fredoka:wght@400;500;600&family=Courgette&family=Roboto:ital,wght@0,400;0,500;0,700;1,500;1,700&display=swap">
<style>
  :root {
    --page: #e9e7ec;
    --navy: #1e2832;
    --navy-deep: #161c23;
    --black: #121212;
    --orange: #ea9a1e;
    --orange-text: #f0a020;
    --red: #b5192d;
    --red-title: #d8262e;
    --white: #ffffff;
    --ink: #151515;
  }
  * { margin: 0; padding: 0; box-sizing: border-box; }
  html, body { width: 1040px; height: 1200px; overflow: hidden; background: var(--page); }
  .stage { position: relative; width: 1040px; height: 1200px; }
  .flyer-frame { position: absolute; left: 70px; top: 20px; width: 900px; height: 1161px; box-shadow: 0 10px 30px rgba(0,0,0,.25); overflow: hidden; }
  .flyer { position: absolute; left: 0; top: 0; width: 580px; height: 748px; transform: scale(1.5517); transform-origin: 0 0; font-family: "Roboto", sans-serif; color: var(--white); }
  .backdrop { position: absolute; inset: 0; }

  .brand { position: absolute; left: 40px; top: 62px; display: flex; align-items: center; gap: 8px; }
  .brand-dot { width: 14px; height: 14px; border-radius: 50%; background: var(--white); }
  .brand-name { font-family: "Fredoka", sans-serif; font-weight: 500; font-size: 20px; color: var(--white); }

  .title-block { position: absolute; right: 32px; top: 58px; text-align: right; }
  .title-main { font-family: "Fredoka", sans-serif; font-weight: 600; font-size: 50px; line-height: 46px; color: var(--orange-text); letter-spacing: 1px; }
  .title-sub { font-family: "Courgette", cursive; font-size: 23px; color: var(--red-title); }
  .hosted { margin-top: 14px; font-size: 10.5px; font-weight: 500; letter-spacing: 1px; }
  .hosted-name { margin-top: 7px; font-size: 10.5px; font-weight: 500; letter-spacing: 2.2px; }
  .rule { margin: 9px 0 0 auto; width: 163px; height: 2px; background: var(--white); }
  .run-note { margin-top: 17px; font-size: 10.5px; font-weight: 500; color: var(--orange-text); line-height: 13px; }

  .schedule { position: absolute; left: 38px; top: 232px; color: var(--ink); }
  .days { font-size: 13px; font-weight: 700; letter-spacing: 2.2px; }
  .cost { margin-top: 8px; font-size: 11px; line-height: 13px; padding-left: 2px; }
  .cost .price { color: var(--red-title); font-weight: 700; }
  .sessions { margin-top: 7px; font-size: 11px; font-weight: 700; font-style: italic; line-height: 13px; padding-left: 2px; }
  .dates { display: flex; gap: 20px; margin-top: 10px; font-size: 8.5px; font-weight: 700; font-style: italic; }
  .date-col h3 { font-size: 8.5px; font-weight: 700; margin-bottom: 9px; }
  .date-col ul { list-style: none; padding-left: 34px; line-height: 11px; }
  .date-col.july ul { padding-left: 10px; }

  .classes { position: absolute; left: 280px; top: 344px; width: 280px; }
  .classes-intro { text-align: center; font-family: "Fredoka", sans-serif; font-weight: 500; font-size: 12.5px; line-height: 16px; }
  .class-cols { display: flex; justify-content: space-between; margin-top: 18px; padding: 0 6px 0 10px; }
  .class-cols ul { list-style: none; font-family: "Fredoka", sans-serif; font-weight: 500; font-size: 12.5px; line-height: 20px; }
  .class-cols li { display: flex; align-items: center; gap: 8px; }
  .class-cols .right li { justify-content: flex-end; }
  .tick { width: 11px; height: 11px; flex: none; }

  .photo { position: absolute; border-radius: 6px; }
  .photo-boy { left: 150px; top: 400px; width: 128px; height: 125px; background: linear-gradient(160deg, #d9453a, #8c2a2a); }
  .photo-girl { left: 40px; top: 495px; width: 186px; height: 122px; background: linear-gradient(160deg, #e08a3c, #6f3d3a); }

  .contact { position: absolute; left: 42px; top: 642px; font-size: 8.5px; font-weight: 700; line-height: 15px; }
  .contact li { list-style: none; display: flex; align-items: center; gap: 6px; }
  .contact svg { width: 8px; height: 8px; }

  .footnote { position: absolute; left: 0; right: 0; top: 690px; text-align: center; font-size: 12px; font-weight: 500; color: var(--orange-text); line-height: 16px; }
</style>
</head>
<body>
<div class="stage">
  <div class="flyer-frame">
    <div class="flyer">
      <svg class="backdrop" viewBox="0 0 580 748" width="580" height="748" aria-hidden="true">
        <rect width="580" height="748" fill="var(--navy)"/>
        <polygon points="0,470 500,605 580,560 580,748 0,748" fill="var(--black)"/>
        <polygon points="415,293 580,235 580,315" fill="var(--navy-deep)"/>
        <polygon points="0,168 415,293 90,420 0,400" fill="var(--orange)"/>
        <line x1="0" y1="165" x2="415" y2="291" stroke="var(--white)" stroke-width="2"/>
        <polygon points="0,400 90,420 0,442" fill="var(--white)"/>
        <polygon points="0,442 90,420 415,293 580,315 580,552 500,606 0,490" fill="var(--red)"/>
        <polygon points="520,560 580,540 580,582" fill="var(--orange)"/>
        <polygon points="350,594 580,562 580,680" fill="var(--white)"/>
      </svg>

      <div class="brand">
        <span class="brand-dot"></span>
        <span class="brand-name">The Tuneful Attic</span>
      </div>

      <header class="title-block">
        <h1 class="title-main">SUNLIT</h1>
        <p class="title-sub">Melody Retreat</p>
        <p class="hosted">HOSTED BY THE TUNEFUL ATTIC</p>
        <p class="hosted-name">SUNLIT MELODY RETREAT</p>
        <div class="rule"></div>
        <p class="run-note">WILL RUN JUNE THROUGH JULY.<br>4 DAYS A WEEK WITH TWO SESSIONS A DAY</p>
      </header>

      <section class="schedule">
        <h2 class="days">Monday- Thursday</h2>
        <p class="cost">Cost is <span class="price">$99.0</span> per session per<br>week. with 25 registration fee</p>
        <p class="sessions">Morning Session 9am-12pm<br>Afternoon Session 1pm-4pm</p>
        <div class="dates">
          <div class="date-col june">
            <h3>June Sessions</h3>
            <ul><li>4th-7th</li><li>11th-16th</li><li>18th-21st</li><li>25th-28th</li></ul>
          </div>
          <div class="date-col july">
            <h3>July Sessions</h3>
            <ul><li>9th-12th</li><li>16th-19th</li><li>23th-26th</li></ul>
          </div>
        </div>
      </section>

      <section class="classes">
        <p class="classes-intro">Students will have the option to choose<br>between the following classes.</p>
        <div class="class-cols">
          <ul class="left">
            <li><svg class="tick" viewBox="0 0 12 12"><circle cx="6" cy="6" r="5.2" fill="none" stroke="#fff" stroke-width="1"/><path d="M3.6 6.2l1.7 1.6 3.1-3.3" fill="none" stroke="#fff" stroke-width="1.1"/></svg>Vocal</li>
            <li><svg class="tick" viewBox="0 0 12 12"><circle cx="6" cy="6" r="5.2" fill="none" stroke="#fff" stroke-width="1"/><path d="M3.6 6.2l1.7 1.6 3.1-3.3" fill="none" stroke="#fff" stroke-width="1.1"/></svg>Guitar</li>
            <li><svg class="tick" viewBox="0 0 12 12"><circle cx="6" cy="6" r="5.2" fill="none" stroke="#fff" stroke-width="1"/><path d="M3.6 6.2l1.7 1.6 3.1-3.3" fill="none" stroke="#fff" stroke-width="1.1"/></svg>Bass</li>
            <li><svg class="tick" viewBox="0 0 12 12"><circle cx="6" cy="6" r="5.2" fill="none" stroke="#fff" stroke-width="1"/><path d="M3.6 6.2l1.7 1.6 3.1-3.3" fill="none" stroke="#fff" stroke-width="1.1"/></svg>Drums</li>
            <li><svg class="tick" viewBox="0 0 12 12"><circle cx="6" cy="6" r="5.2" fill="none" stroke="#fff" stroke-width="1"/><path d="M3.6 6.2l1.7 1.6 3.1-3.3" fill="none" stroke="#fff" stroke-width="1.1"/></svg>Violin</li>
            <li><svg class="tick" viewBox="0 0 12 12"><circle cx="6" cy="6" r="5.2" fill="none" stroke="#fff" stroke-width="1"/><path d="M3.6 6.2l1.7 1.6 3.1-3.3" fill="none" stroke="#fff" stroke-width="1.1"/></svg>Rock Band</li>
          </ul>
          <ul class="right">
            <li>Sound Mixing<svg class="tick" viewBox="0 0 12 12"><circle cx="6" cy="6" r="5.2" fill="none" stroke="#fff" stroke-width="1"/><path d="M3.6 6.2l1.7 1.6 3.1-3.3" fill="none" stroke="#fff" stroke-width="1.1"/></svg></li>
            <li>Video Making<svg class="tick" viewBox="0 0 12 12"><circle cx="6" cy="6" r="5.2" fill="none" stroke="#fff" stroke-width="1"/><path d="M3.6 6.2l1.7 1.6 3.1-3.3" fill="none" stroke="#fff" stroke-width="1.1"/></svg></li>
            <li>DJ /Mixing<svg class="tick" viewBox="0 0 12 12"><circle cx="6" cy="6" r="5.2" fill="none" stroke="#fff" stroke-width="1"/><path d="M3.6 6.2l1.7 1.6 3.1-3.3" fill="none" stroke="#fff" stroke-width="1.1"/></svg></li>
            <li>Song Writing<svg class="tick" viewBox="0 0 12 12"><circle cx="6" cy="6" r="5.2" fill="none" stroke="#fff" stroke-width="1"/><path d="M3.6 6.2l1.7 1.6 3.1-3.3" fill="none" stroke="#fff" stroke-width="1.1"/></svg></li>
            <li>Recording<svg class="tick" viewBox="0 0 12 12"><circle cx="6" cy="6" r="5.2" fill="none" stroke="#fff" stroke-width="1"/><path d="M3.6 6.2l1.7 1.6 3.1-3.3" fill="none" stroke="#fff" stroke-width="1.1"/></svg></li>
            <li>Hip-Hop Boot Camp<svg class="tick" viewBox="0 0 12 12"><circle cx="6" cy="6" r="5.2" fill="none" stroke="#fff" stroke-width="1"/><path d="M3.6 6.2l1.7 1.6 3.1-3.3" fill="none" stroke="#fff" stroke-width="1.1"/></svg></li>
          </ul>
        </div>
      </section>

      <div class="photo photo-boy" role="img" aria-label="Photo of a young boy sitting cross-legged playing an acoustic guitar"></div>
      <div class="photo photo-girl" role="img" aria-label="Photo of a young girl sitting cross-legged playing an acoustic guitar"></div>

      <ul class="contact">
        <li><svg viewBox="0 0 10 10"><path d="M2 1l2 2-1 1.2c.6 1.2 1.6 2.2 2.8 2.8L7 6l2 2-1.2 1.3C4.5 9 1 5.5.7 2.2z" fill="#fff"/></svg>555 018 2740</li>
        <li><svg viewBox="0 0 10 10"><path d="M5 .5a3.3 3.3 0 0 0-3.3 3.3C1.7 6.3 5 9.5 5 9.5s3.3-3.2 3.3-5.7A3.3 3.3 0 0 0 5 .5zm0 4.6a1.3 1.3 0 1 1 0-2.6 1.3 1.3 0 0 1 0 2.6z" fill="#fff"/></svg>2480 N LARK AVE FERNHILL FL</li>
      </ul>

      <p class="footnote">Space is limited, campers are allowed to sign up for morning and afternoon sessions,<br>campers will need to bring their own lunch if taking both sessions.</p>
    </div>
  </div>
</div>
</body>
</html>
```